Business Card Design

Hoping for a black background business card, minimalistic design.
With the Marble Crest logo you created in white.

I would like to include:
My Name and title
Address (street address)
Reception: (phone number)
Fax: (fax number)
Reception: (email address)
Direct email: (email address)
Instagram: (ig handle)

```html
<!DOCTYPE html>
<html lang="en">
<head>
<meta charset="utf-8">
<title>Marble Crest — Business Card</title>
<link href="https://fonts.googleapis.com/css2?family=Montserrat:wght@400;500&family=Oswald:wght@600&display=swap" rel="stylesheet">
<style>
  :root {
    --backdrop: #d9d6d2;
    --card: #121212;
    --card-edge: #1c1c1c;
    --ink: #ffffff;
    --ink-soft: #d8d8d8;
  }
  * { margin: 0; padding: 0; box-sizing: border-box; }
  html, body { width: 1200px; height: 716px; overflow: hidden; }
  body {
    background: var(--backdrop);
    display: flex;
    align-items: center;
    justify-content: center;
    gap: 60px;
    font-family: "Montserrat", sans-serif;
    color: var(--ink);
  }
  .card {
    width: 520px;
    height: 297px;
    background: linear-gradient(135deg, var(--card-edge), var(--card));
    border-radius: 8px;
    box-shadow: 0 10px 28px rgba(0,0,0,0.25);
    position: relative;
  }
  /* Front */
  .card-front {
    display: flex;
    align-items: center;
    justify-content: center;
    gap: 18px;
  }
  .brand-dot {
    width: 62px; height: 62px;
    border: 3px solid var(--ink);
    border-radius: 50%;
  }
  .brand-divider {
    width: 1px; height: 80px;
    background: var(--ink);
    opacity: 0.8;
  }
  .brand-name {
    font-weight: 400;
    font-size: 30px;
    letter-spacing: 3px;
    text-transform: uppercase;
  }
  /* Back */
  .card-back {
    display: flex;
    align-items: center;
    padding: 0 28px 0 36px;
  }
  .identity {
    width: 210px;
    text-align: right;
    padding-right: 22px;
  }
  .person-name {
    font-family: "Oswald", sans-serif;
    font-weight: 600;
    font-size: 32px;
    line-height: 1;
    text-transform: uppercase;
    letter-spacing: 0.5px;
  }
  .person-title {
    margin-top: 6px;
    font-size: 13px;
    letter-spacing: 2px;
    color: var(--ink-soft);
    text-transform: uppercase;
  }
  .back-divider {
    width: 1px; height: 150px;
    background: var(--ink);
    opacity: 0.8;
  }
  .contact-list {
    list-style: none;
    padding-left: 20px;
    font-size: 13.5px;
    line-height: 1.55;
  }
  .contact-list li { display: flex; align-items: center; gap: 7px; }
  .contact-list .no-icon { padding-left: 18px; }
  .contact-icon { width: 11px; height: 11px; flex: none; }
</style>
</head>
<body>
  <section class="card card-front" aria-label="Card front">
    <span class="brand-dot"></span>
    <span class="brand-divider"></span>
    <span class="brand-name">Marble Crest</span>
  </section>

  <section class="card card-back" aria-label="Card back">
    <div class="identity">
      <p class="person-name">Daniel Reyes</p>
      <p class="person-title">Director</p>
    </div>
    <span class="back-divider"></span>
    <ul class="contact-list">
      <li class="no-icon">482 Harlow Ave, Suite 210</li>
      <li class="no-icon">Brookfield, NY 11590</li>
      <li>
        <svg class="contact-icon" viewBox="0 0 12 12"><path d="M3 1 L5 3.5 L4 5 Q5.5 7 7 8 L8.5 7 L11 9 L9.5 11 Q5 10.5 1 3 Z" fill="#fff"/></svg>
        555-014-2273
      </li>
      <li>
        <svg class="contact-icon" viewBox="0 0 12 12"><rect x="3" y="1" width="6" height="3" fill="none" stroke="#fff" stroke-width="1.2"/><rect x="1" y="4" width="10" height="5" rx="1" fill="#fff"/><rect x="3" y="8" width="6" height="3" fill="#fff"/></svg>
        555-019-6648
      </li>
      <li>
        <svg class="contact-icon" viewBox="0 0 12 12"><rect x="1" y="2.5" width="10" height="7" fill="none" stroke="#fff" stroke-width="1.2"/><path d="M1 2.5 L6 6.5 L11 2.5" fill="none" stroke="#fff" stroke-width="1.2"/></svg>
        marble@crest.com
      </li>
      <li>
        <svg class="contact-icon" viewBox="0 0 12 12"><rect x="1" y="2.5" width="10" height="7" fill="none" stroke="#fff" stroke-width="1.2"/><path d="M1 2.5 L6 6.5 L11 2.5" fill="none" stroke="#fff" stroke-width="1.2"/></svg>
        info@marblecrest.com
      </li>
      <li>
        <svg class="contact-icon" viewBox="0 0 12 12"><circle cx="6" cy="6" r="4.5" fill="none" stroke="#fff" stroke-width="1.2"/></svg>
        @marblecrest.com
      </li>
    </ul>
  </section>
</body>
</html>
```